Lumer product box design professional skincare

Design a professional skincare box that looks clean and modern. Based on the label. We need a professional look. It needs to be outstanding from other brands on the market. It is going to be a luxury market product. The box should fit multiple products, so the box should stay multifunctional, yet very professional.

Target Market(s)

skincare, beauty

Industry/Entity Type

Skin Care Product

Requirements
Must have
• Include logo
• Include: Professional Skincare Therapies

```html
<!DOCTYPE html>
<html lang="en">
<head>
<meta charset="utf-8">
<title>Lumer – Japanese Sakura Mask box</title>
<link href="https://fonts.googleapis.com/css2?family=Questrial&family=Roboto+Condensed:wght@400;700&family=PT+Sans&display=swap" rel="stylesheet">
<style>
  :root {
    --stage: #cbcbcb;
    --panel-front: #dedede;
    --panel-side: #ffffff;
    --band: #a9a9a9;
    --ink: #111111;
    --gold: #a07812;
  }
  * { margin: 0; padding: 0; box-sizing: border-box; }
  html, body { width: 1200px; height: 1029px; overflow: hidden; background: var(--stage); }
  .box-net {
    position: absolute; left: 230px; top: 45px;
    width: 740px; height: 940px; display: flex;
  }
  .panel { position: relative; height: 100%; overflow: hidden; }
  .panel-side { width: 300px; background: var(--panel-side); border-right: 1px solid #c4c4c4; }
  .panel-front { width: 440px; background: var(--panel-front); }

  .band { position: absolute; left: 145px; width: 155px; background: var(--band); }
  .band-top { top: 0; height: 215px; }
  .band-bottom { top: 715px; bottom: 0; }

  .rotated { position: absolute; white-space: nowrap; transform: translate(-50%, -50%) rotate(-90deg); }
  .brand-name { font-family: "Questrial", sans-serif; color: var(--ink); line-height: 1; letter-spacing: 2px; }
  .side-brand { left: 132px; top: 420px; font-size: 92px; }
  .side-tagline { left: 200px; top: 420px; font-family: "PT Sans", sans-serif; font-size: 18px; color: var(--gold); }
  .front-brand { left: 132px; top: 413px; font-size: 128px; }

  .info-line { position: absolute; left: 202px; color: var(--ink); white-space: nowrap; line-height: 1.2; }
  .product-name-main { top: 300px; font-family: "Questrial", sans-serif; font-size: 29px; letter-spacing: 0.5px; }
  .product-name-sub { top: 337px; font-family: "Questrial", sans-serif; font-size: 21px; letter-spacing: 0.5px; }
  .claim { top: 428px; font-family: "Roboto Condensed", sans-serif; font-weight: 700; font-size: 17px; line-height: 1.35; }
  .ingredients-intro { top: 518px; font-family: "Roboto Condensed", sans-serif; font-size: 11.5px; line-height: 1.6; }
  .ingredients-list { top: 553px; font-family: "Roboto Condensed", sans-serif; font-weight: 700; font-size: 14.5px; line-height: 1.38; }
  .front-tagline {
    position: absolute; left: 99px; top: 628px;
    font-family: "PT Sans", sans-serif; font-size: 19px; color: var(--gold); white-space: nowrap;
  }
</style>
</head>
<body>
  <div class="box-net">
    <section class="panel panel-side">
      <div class="rotated brand-name side-brand">lumer</div>
      <div class="rotated side-tagline">Professional Skincare Therapies</div>
    </section>
    <section class="panel panel-front">
      <div class="band band-top"></div>
      <div class="band band-bottom"></div>
      <div class="rotated brand-name front-brand">lumer</div>
      <h1 class="info-line product-name-main">JAPANESE</h1>
      <h2 class="info-line product-name-sub">SAKURA MASK</h2>
      <p class="info-line claim">NON-SURGERY<br>FACELIFT THERAPY</p>
      <p class="info-line ingredients-intro">Ingredients that have Scientific<br>Proof of Anti Aging:</p>
      <p class="info-line ingredients-list">Cherry blossom extact,<br>Collegen, Hyaluronic Acid,<br>Coconut Oil.</p>
      <p class="front-tagline">Professional Skincare Therapies</p>
    </section>
  </div>
</body>
</html>
```